Outpatient Mental Health Clinic needs a good brochure

We are an outpatient clinic in Michigan, USA and provide therapy and evaluation services for adults, adolescents, and children. Our psychologists, social workers, and counselors help individuals who present with a host of psychological difficulties. Our goal for the brochure is to give an overview of our services so that our marketing person can pass them out to physicians and other referral sources.

Target Market(s)

Our target market are patients who are seeking referrals through their primary care physicians.

Industry/Entity Type

Clinic

Font styles to use
Serif
Sans Serif

Colors
fbf289
f68d4c
f37122
ffffff

Requirements
Must have
• My project must be illustrative enough to show what services are provided. Pictures of individuals is also important.
Nice to have
• In addition to content I would like to have pictures of individuals.

```html
<!DOCTYPE html>
<html lang="en">
<head>
<meta charset="UTF-8">
<title>Lakeshore Mind – Tri-fold Brochure</title>
<link href="https://fonts.googleapis.com/css2?family=Montserrat:wght@400;600;800&family=Open+Sans:wght@400;600&display=swap" rel="stylesheet">
<style>
  :root{
    --orange:#f37122;
    --orange-soft:#f68d4c;
    --sun:#fbf289;
    --paper:#ffffff;
    --mist:#f6f3ea;
    --ink:#55585c;
    --stage:#dcdcdc;
  }
  *{box-sizing:border-box;margin:0;padding:0}
  html,body{width:1200px;height:800px;overflow:hidden;background:var(--stage)}
  .brochure{position:absolute;left:60px;top:20px;width:1080px;height:760px;background:var(--paper);box-shadow:0 6px 20px rgba(0,0,0,.18);overflow:hidden}
  .shapes,.photo{position:absolute;left:0;top:0}
  .panel{position:absolute;top:0;width:360px;height:760px}
  .panel--about{left:0}
  .panel--services{left:360px}
  .panel--cover{left:720px}
  .heading-box{position:absolute;left:30px;top:50px;width:300px;min-height:80px;border:2px solid var(--orange);border-bottom:8px solid var(--orange);padding:20px 18px 16px}
  .heading-box h2{font-family:"Montserrat",sans-serif;font-weight:400;color:var(--orange);font-size:30px;line-height:1.1}
  .about-text{position:absolute;left:30px;top:160px;width:300px;font-family:"Open Sans",sans-serif;font-size:15.5px;line-height:1.36;color:var(--ink);text-align:justify}
  .service-list{position:absolute;left:34px;top:160px;width:300px;list-style:none;font-family:"Open Sans",sans-serif;font-size:14.5px;line-height:1.25;color:var(--ink)}
  .service-list li{position:relative;padding-left:26px;margin-bottom:14px}
  .service-list li::before{content:"";position:absolute;left:2px;top:3px;width:10px;height:10px;border-radius:50%;border:3px solid var(--orange);background:var(--paper)}
  .brand{font-family:"Montserrat",sans-serif;color:var(--orange);font-weight:800;letter-spacing:.5px;white-space:nowrap}
  .brand-sub{font-family:"Montserrat",sans-serif;font-weight:800;font-size:12px;color:var(--orange);letter-spacing:.3px;white-space:nowrap}
  .cover-brand{position:absolute;left:36px;top:42px}
  .cover-brand .brand{font-size:27px}
  .back-contact{position:absolute;left:36px;top:580px;color:var(--paper);font-family:"Open Sans",sans-serif}
  .back-contact .brand{color:var(--paper);font-size:22px}
  .back-contact .brand-sub{color:var(--sun);font-size:10.5px;margin:2px 0 12px}
  .back-contact p{font-size:14px;line-height:1.4}
</style>
</head>
<body>
<main class="brochure">
  <svg class="shapes" width="1080" height="760" viewBox="0 0 1080 760" aria-hidden="true">
    <rect x="360" y="0" width="720" height="760" fill="var(--mist)"/>
    <path d="M360 560 C520 500 640 420 720 300 L720 760 L360 760 Z" fill="var(--orange)"/>
    <path d="M720 300 C760 250 800 200 860 170 C960 130 1040 110 1080 100 L1080 760 L720 760 Z" fill="var(--orange)"/>
    <path d="M760 310 C820 250 900 210 1080 170 L1080 200 C940 230 860 270 800 330 Z" fill="var(--orange-soft)"/>
    <line x1="360" y1="0" x2="360" y2="760" stroke="rgba(0,0,0,.06)"/>
    <line x1="720" y1="0" x2="720" y2="760" stroke="rgba(0,0,0,.06)"/>
  </svg>

  <svg class="photo" width="360" height="760" viewBox="0 0 360 760" role="img" aria-label="Photo of a smiling child sitting with a parent during a family session">
    <defs><linearGradient id="childTone" x1="0" y1="0" x2="0" y2="1"><stop offset="0" stop-color="#fdf6b8"/><stop offset="1" stop-color="#f9b98a"/></linearGradient></defs>
    <path d="M0 520 C110 470 250 450 360 420 L360 760 L0 760 Z" fill="url(#childTone)"/>
    <path d="M0 520 C110 470 250 450 360 420" fill="none" stroke="var(--orange)" stroke-width="6"/>
  </svg>

  <svg class="photo" width="1080" height="760" viewBox="0 0 1080 760" role="img" aria-label="Photo of a psychologist in a bright office reviewing notes on a tablet">
    <defs><linearGradient id="clinicianTone" x1="0" y1="0" x2="1" y2="1"><stop offset="0" stop-color="#fffdf4"/><stop offset="1" stop-color="#f3e6d6"/></linearGradient></defs>
    <polygon points="810,340 1080,190 1080,760 960,760" fill="url(#clinicianTone)" stroke="rgba(0,0,0,.12)" stroke-width="2"/>
  </svg>

  <section class="panel panel--about">
    <div class="heading-box"><h2>About Us</h2></div>
    <p class="about-text">Lakeshore Mind is an outpatient mental health clinic in Michigan offering therapy and evaluation for adults, adolescents and children. Our psychologists, social workers and counselors work with people facing a wide range of emotional and psychological difficulties, in close partnership with referring physicians to give every patient timely, caring support.</p>
  </section>

  <section class="panel panel--services">
    <div class="heading-box"><h2>Our Services</h2></div>
    <ul class="service-list">
      <li>Individual therapy for adults, adolescents and children</li>
      <li>Psychological and diagnostic evaluations</li>
      <li>Family and couples counseling sessions</li>
      <li>Care for anxiety, depression, ADHD and trauma</li>
    </ul>
    <div class="back-contact">
      <div class="brand">LAKESHORE MIND</div>
      <div class="brand-sub">OUTPATIENT MENTAL HEALTH CLINIC</div>
      <p>214 Harbor Ave, Grand Haven, MI<br>Phone 616.555.0142<br>Email: hello@lakeshoremind.org</p>
    </div>
  </section>

  <section class="panel panel--cover">
    <div class="cover-brand">
      <div class="brand">LAKESHORE MIND</div>
      <div class="brand-sub">OUTPATIENT MENTAL HEALTH CLINIC</div>
    </div>
  </section>
</main>
</body>
</html>
```